Buch-/eBook-Cover für populär-wissenschaftliches Buch
Zielgruppe
Der Talgrund-Verlag veröffentlicht Bücher zu psychologischen Themen. Dies ist ein eher populär wissenschaftliches Buch für eine breite Leserschaft.
Aufgabenstellung
Benötigt wird ein Buchcover für KTZ, Papierformat 158*223, Buchformat 154 x 3 x 217 mm 272 Normseiten
Kurzbeschreibung
Am Ufer getragen?
Fragen sich die Autoren Konrad Brüning und Matthias Oswerk. Zwei Psychoanalytiker mit langer Berufserfahrung. Geht das überhaupt: in Liebe und vereint zu sein? Dazu müssen zunächst andere Fragen geklärt werden.
Was vereint die Geschlechter, was bringt sie zusammen? Liebe? Dieses Wort gab es im Deutschen im frühen Mittelalter nicht, erst im späteren. In manchen Kulturen gibt es dieses Wort bis heute nicht, und dennoch leben Mann und Frau zusammen. Schon seit Jahrtausenden beschäftigt sich der Mensch mit der Beziehung zwischen den Geschlechtern. Philosophen, Schriftsteller, Dichter, Maler, Musiker, später Psychoanalytiker, Anthropologen und Soziologen hat die Beziehung zwischen Mann und Frau intensiv beschäftigt. Auch die Religionen befassen sich mit der Beziehung zwischen den Geschlechtern und zeigen vorwiegend auf moralischen und idealistischen Ebenen Umgangsweisen und Lebensformen zwischen den Geschlechtern auf.
280 Normseiten
Bitte Klappentext auf Rückseite

```html
<!DOCTYPE html>
<html lang="de">
<head>
<meta charset="utf-8">
<title>Am Ufer getragen? – Buchcover</title>
<link href="https://fonts.googleapis.com/css2?family=Bebas+Neue&family=Barlow:wght@600&display=swap" rel="stylesheet">
<style>
  :root {
    --title-red: #c8202a;
    --paper-top: #ffffff;
    --paper-bottom: #e2e5e8;
    --spine-top: #f4f5f6;
    --spine-mid: #d3d7da;
    --spine-bottom: #5d6266;
    --spine-author: #3a3e42;
    --band-dark: #2e1219;
    --band-mid: #5a2631;
    --stripe-purple: #5b1848;
    --author-white: #f4f1f1;
  }
  html, body {
    margin: 0;
    padding: 0;
    width: 930px;
    height: 1200px;
    overflow: hidden;
    background: #ffffff;
  }
  .book {
    position: relative;
    width: 930px;
    height: 1200px;
    overflow: hidden;
    display: flex;
  }

  /* Spine */
  .spine {
    position: relative;
    width: 90px;
    height: 1200px;
    flex: none;
    background: linear-gradient(180deg, var(--spine-top) 0%, var(--spine-mid) 55%, var(--spine-bottom) 100%);
    box-shadow: inset -3px 0 6px rgba(0,0,0,0.12);
  }
  .spine-title {
    position: absolute;
    top: 70px;
    left: 50%;
    transform: translateX(-50%);
    margin: 0;
    writing-mode: vertical-rl;
    font-family: "Bebas Neue", "Oswald", sans-serif;
    font-weight: 400;
    font-size: 66px;
    line-height: 1;
    letter-spacing: 1px;
    color: var(--title-red);
    white-space: nowrap;
  }
  .spine-authors {
    position: absolute;
    top: 690px;
    left: 50%;
    transform: translateX(-50%);
    margin: 0;
    writing-mode: vertical-rl;
    font-family: "Barlow", "Arial", sans-serif;
    font-weight: 600;
    font-size: 16px;
    letter-spacing: 1px;
    color: var(--spine-author);
    white-space: nowrap;
  }

  /* Front cover */
  .cover {
    position: relative;
    width: 840px;
    height: 1200px;
    flex: none;
    overflow: hidden;
    background: linear-gradient(180deg, var(--paper-top) 0%, var(--paper-bottom) 54%);
  }
  .title-block {
    position: absolute;
    top: 0;
    left: 0;
    width: 100%;
    color: var(--title-red);
    font-family: "Bebas Neue", "Oswald", sans-serif;
    text-align: center;
  }
  .rule-row {
    position: absolute;
    left: 0;
    width: 100%;
    display: flex;
    align-items: center;
    justify-content: center;
    gap: 22px;
  }
  .rule {
    height: 4px;
    background: var(--title-red);
  }
  .title-small {
    font-size: 62px;
    line-height: 1;
  }
  .rule-row--top { top: 92px; }
  .rule-row--top .rule { width: 200px; }
  .rule-row--bottom { top: 528px; }
  .rule-row--bottom .rule { width: 260px; }
  .title-main {
    position: absolute;
    top: 150px;
    left: 0;
    width: 100%;
    margin: 0;
    font-weight: 400;
    font-size: 212px;
    line-height: 0.8;
    letter-spacing: 2px;
  }
  .title-main span { display: block; }

  .lower-band {
    position: absolute;
    left: 0;
    top: 640px;
    width: 100%;
    height: 560px;
    background: radial-gradient(ellipse at 50% 45%, var(--band-mid) 0%, var(--band-dark) 85%);
  }
  .accent-stripe {
    position: absolute;
    left: 0;
    top: 0;
    width: 100%;
    height: 14px;
    background: var(--stripe-purple);
  }
  .artwork {
    position: absolute;
    left: 90px;
    top: 60px;
    width: 660px;
    height: 380px;
    border-radius: 40px 40px 10px 10px;
    background: linear-gradient(90deg, rgba(230,110,50,0.85) 0%, rgba(200,80,160,0.75) 30%, rgba(220,170,120,0.8) 50%, rgba(110,190,70,0.75) 70%, rgba(50,120,200,0.85) 100%);
    filter: blur(2px);
  }
  .authors {
    position: absolute;
    left: 0;
    bottom: 40px;
    width: 100%;
    margin: 0;
    text-align: center;
    font-family: "Barlow", "Arial", sans-serif;
    font-weight: 600;
    font-size: 30px;
    letter-spacing: 2px;
    color: var(--author-white);
  }
</style>
</head>
<body>
  <div class="book">
    <aside class="spine">
      <p class="spine-title">Am Ufer getragen?</p>
      <p class="spine-authors">KONRAD BRÜNING and MATTHIAS OSWERK</p>
    </aside>
    <main class="cover">
      <header class="title-block">
        <div class="rule-row rule-row--top">
          <span class="rule"></span>
          <span class="title-small">Am</span>
          <span class="rule"></span>
        </div>
        <h1 class="title-main" aria-label="Am Ufer getragen?">
          <span>Ufer</span>
          <span>getragen</span>
        </h1>
        <div class="rule-row rule-row--bottom">
          <span class="rule"></span>
          <span class="title-small">?</span>
          <span class="rule"></span>
        </div>
      </header>
      <section class="lower-band">
        <div class="accent-stripe"></div>
        <div class="artwork" role="img" aria-label="Illustration: eine dicht gedrängte Gruppe bunter Holzfiguren in Regenbogenfarben mit verstreuten Holzklötzchen"></div>
        <p class="authors">KONRAD BRÜNING and MATTHIAS OSWERK</p>
      </section>
    </main>
  </div>
</body>
</html>
```